Brightmold Laser Lipo Brochure

Need a 3 panel brochure
Full Colour
Sales/info brochure
Photos provided
Testimonials
Product Specs - http://brightmoldcontour.com/brightmoldcontour/request-a-demo/opportunity.aspx
Brightmold Laser Lipo is trademarked
Website and contact details
description of what about the technique-
http://brightmoldcontour.com/brightmoldcontour/laser-lipo.aspx
Examples of successful clinics - to follow

Also require business card to compliment the brochure

Target Market(s)

Target Audience Clinics, Gyms, Salons

Industry/Entity Type

Business

Requirements
Must have
• website www.brightmoldcontour.com
testimonials
"After just two laser-lipo sessions I was happily surprised to find that I had dropped between one and two belt sizes ..... dinewise.com.au TKM"
"I have been a number of the laser lipo treatments and using the VNA cream in between session with great results. Have lost 4cm around waist. Highly recommend.....dinewise.com.au MarnieS"

```html
<!DOCTYPE html>
<html lang="en">
<head>
<meta charset="utf-8">
<title>Brightmold Laser Lipo – Business Card Set</title>
<link rel="stylesheet" href="https://fonts.googleapis.com/css2?family=Open+Sans:ital,wght@0,300;0,400;0,600;1,400;1,600&display=swap">
<style>
  :root {
    --sheet-bg: #ebe6e1;
    --card-bg: #ffffff;
    --card-edge: #d9d3cd;
    --ink: #1c1c1c;
    --ink-soft: #3a3a3a;
    --ink-muted: #555555;
    --rule: #8a8a8a;
    --label: #1a1a1a;
    --photo-light: #f1e3d6;
    --photo-mid: #d9b79c;
    --photo-deep: #b98f72;
  }
  * { box-sizing: border-box; margin: 0; padding: 0; }
  html, body { width: 1200px; height: 788px; overflow: hidden; }
  body {
    background: var(--sheet-bg);
    font-family: "Open Sans", Arial, sans-serif;
    color: var(--ink);
    position: relative;
  }
  .view-label {
    position: absolute;
    width: 526px;
    text-align: center;
    font-size: 20px;
    font-weight: 400;
    color: var(--label);
  }
  .card {
    position: absolute;
    width: 526px;
    height: 300px;
    background: var(--card-bg);
    border: 1px solid var(--card-edge);
    border-radius: 22px;
    overflow: hidden;
  }
  .col-left  { left: 54px; }
  .col-right { left: 622px; }
  .row-top    { top: 74px; }
  .row-bottom { top: 445px; }
  .label-top    { top: 33px; }
  .label-bottom { top: 403px; }

  .brand {
    position: absolute;
    text-align: right;
    color: var(--ink);
  }
  .brand-name {
    display: block;
    font-weight: 300;
    font-size: 50px;
    line-height: 1;
    letter-spacing: 0.5px;
  }
  .brand-descriptor {
    display: block;
    font-weight: 400;
    font-size: 19px;
    line-height: 1.2;
    margin-top: 4px;
    color: var(--ink-soft);
  }
  .tagline {
    position: absolute;
    font-style: italic;
    font-size: 17px;
    color: var(--ink);
    white-space: nowrap;
  }
  .web {
    position: absolute;
    font-size: 16px;
    letter-spacing: 2.6px;
    color: var(--ink-soft);
    white-space: nowrap;
  }

  /* Front */
  .contact {
    position: absolute;
    left: 0; right: 0;
    top: 170px;
    text-align: center;
    font-size: 13px;
    color: var(--ink-soft);
    line-height: 20px;
  }
  .contact .person { font-size: 16px; margin-bottom: 6px; }
  .contact .person small { font-size: 13px; }
  .contact .key { font-weight: 600; font-style: italic; color: var(--ink); }
  .contact .address { margin-top: 7px; }

  /* Back 2 */
  .photo-area {
    position: absolute;
    left: 0; bottom: 0;
    width: 180px; height: 270px;
    background: radial-gradient(ellipse at 50% 60%, var(--photo-mid) 0%, var(--photo-light) 55%, rgba(255,255,255,0) 75%),
                linear-gradient(180deg, rgba(255,255,255,0) 0%, var(--photo-deep) 140%);
  }

  /* Back 3 */
  .hours {
    position: absolute;
    left: 0; right: 0;
    top: 190px;
    text-align: center;
    color: var(--ink-soft);
  }
  .hours .rule {
    width: 110px; height: 1px;
    background: var(--rule);
    margin: 0 auto;
  }
  .hours h2 {
    font-size: 15px;
    font-weight: 600;
    margin-top: 9px;
    color: var(--ink);
  }
  .hours p {
    font-size: 13px;
    margin: 4px 0 9px;
  }
  .hours .divider { margin: 0 8px; color: var(--rule); }
</style>
</head>
<body>

  <div class="view-label col-left label-top">Front</div>
  <div class="view-label col-right label-top">Back - 1</div>
  <div class="view-label col-left label-bottom">Back - 2</div>
  <div class="view-label col-right label-bottom">Back - 3</div>

  <!-- Front -->
  <section class="card card-front col-left row-top">
    <div class="brand" style="left:170px; top:48px; width:246px;">
      <span class="brand-name">Brightmold</span>
      <span class="brand-descriptor">laser lipo</span>
    </div>
    <p class="tagline" style="left:156px; top:126px;">“Now you can keep it off forever!”</p>
    <div class="contact">
      <p class="person">Your Name, <small>Designation</small></p>
      <p><span class="key">phone</span> 0400 555 218</p>
      <p><span class="key">email</span> mara@brightmoldcontour.com</p>
      <p><span class="key">fax</span> www.brightmoldcontour.com</p>
      <p class="address">14 Carramar Lane, Rear Entrance, Lakeview 6030</p>
    </div>
  </section>

  <!-- Back 1 -->
  <section class="card card-back col-right row-top">
    <div class="brand" style="left:170px; top:82px; width:276px;">
      <span class="brand-name" style="font-size:54px;">Brightmold</span>
      <span class="brand-descriptor">laser lipo</span>
    </div>
    <p class="tagline" style="left:140px; top:157px;">“Now you can keep it off forever!”</p>
    <p class="web" style="left:122px; top:261px;">www.brightmoldcontour.com</p>
  </section>

  <!-- Back 2 -->
  <section class="card card-back-photo col-left row-bottom">
    <div class="photo-area" role="img" aria-label="Photo of a slim waist with a measuring tape wrapped around the hips"></div>
    <div class="brand" style="left:140px; top:30px; width:262px;">
      <span class="brand-name">Brightmold</span>
      <span class="brand-descriptor">laser lipo</span>
    </div>
    <p class="tagline" style="left:118px; top:120px;">“Now you can keep it off forever!”</p>
    <p class="web" style="left:280px; top:257px; letter-spacing:0.3px;">www.brightmoldcontour.com</p>
  </section>

  <!-- Back 3 -->
  <section class="card card-back-hours col-right row-bottom">
    <div class="brand" style="left:170px; top:32px; width:276px;">
      <span class="brand-name" style="font-size:54px;">Brightmold</span>
      <span class="brand-descriptor">laser lipo</span>
    </div>
    <p class="tagline" style="left:140px; top:133px;">“Now you can keep it off forever!”</p>
    <div class="hours">
      <div class="rule"></div>
      <h2>Hours of Operation</h2>
      <p>Mon - Fri 8am - 7pm<span class="divider">|</span>Saturday 8am - 2pm</p>
      <div class="rule"></div>
    </div>
    <p class="web" style="left:122px; top:258px;">www.brightmoldcontour.com</p>
  </section>

</body>
</html>
```